Energy trading company (Voltrisa) needs a business card

We need a business card for a company based in Central America. Our main purpose is trading energy . We already have the logo but we need some good creativity to design a high impact business card. Colors blue, orange, green can be used or we would like to see good combinatios with our logo

Target Market(s)

Energy

Industry/Entity Type

Power Generation

Contact Information for Business Card

Logo , headquarters , name, background

Font styles to use
Serif
Sans Serif

Colors

Designer to choose colors to be used in the design.

Requirements
Must have
• it must have a fresh and clean view
Nice to have
• good backgrounds that combine with the logo
Should not have
• too much words

```html
<!DOCTYPE html>
<html lang="en">
<head>
<meta charset="utf-8">
<title>Voltrisa – Business Card</title>
<link rel="stylesheet" href="https://fonts.googleapis.com/css2?family=Questrial&family=Oswald:wght@500&family=Roboto:wght@400&display=swap">
<style>
  :root {
    --orange: #f0a21e;
    --orange-deep: #e8961a;
    --orange-light: #f6bf2c;
    --charcoal: #252525;
    --white: #ffffff;
    --backdrop: #e9e6e1;
    --ring: #ffffff;
  }
  * { box-sizing: border-box; margin: 0; padding: 0; }
  html, body { width: 1200px; height: 780px; overflow: hidden; }
  body { background: var(--backdrop); position: relative; }

  .card { position: absolute; overflow: hidden; box-shadow: 0 10px 28px rgba(0,0,0,.18); }

  /* Front */
  .card-front { left: 60px; top: 213px; width: 620px; height: 354px; background: var(--white); }
  .brand { position: absolute; left: 44px; top: 96px; display: flex; align-items: center; gap: 16px; }
  .brand-dot { width: 46px; height: 46px; border-radius: 50%; background: var(--orange); }
  .brand-name { font-family: "Questrial", sans-serif; font-size: 58px; letter-spacing: 2px; color: var(--orange); text-transform: uppercase; line-height: 1; }

  .title-stripe { position: absolute; left: 0; top: 224px; width: 100%; height: 27px; background: var(--orange-light); padding-left: 34px; display: flex; align-items: center; }
  .person { font-family: "Oswald", sans-serif; font-weight: 500; font-size: 17px; color: var(--white); text-transform: uppercase; letter-spacing: .3px; }
  .person .divider { margin: 0 8px; }
  .person .role { font-size: 14px; }

  .contact-band { position: absolute; left: 0; top: 251px; width: 100%; height: 103px; background: var(--charcoal); padding: 20px 0 0 34px; }
  .contact-line { display: flex; align-items: center; gap: 9px; font-family: "Roboto", sans-serif; font-size: 15px; color: var(--white); height: 22px; }
  .contact-icon { width: 16px; height: 16px; flex: none; }

  .mark-notch { position: absolute; left: 410px; top: 36px; width: 220px; height: 220px; border-radius: 50%; background: var(--white); }
  .mark-disc { position: absolute; left: 432px; top: 48px; width: 176px; height: 176px; border-radius: 50%; background: var(--orange); }

  /* Back */
  .card-back { left: 790px; top: 128px; width: 300px; height: 525px; }
  .back-field { position: absolute; inset: 0; background: radial-gradient(circle at 50% 40%, #f6c22c 0%, #f0a520 60%, #e8961a 100%); }
  .back-brand { position: absolute; left: 40px; bottom: 66px; display: flex; align-items: center; gap: 10px; }
  .back-dot { width: 26px; height: 26px; border-radius: 50%; background: var(--white); }
  .back-name { font-family: "Questrial", sans-serif; font-size: 30px; color: var(--white); text-transform: uppercase; letter-spacing: 1px; }
</style>
</head>
<body>

<section class="card card-front">
  <div class="brand">
    <span class="brand-dot"></span>
    <span class="brand-name">Voltrisa</span>
  </div>

  <div class="title-stripe">
    <p class="person">Marcus Delgado<span class="divider">|</span><span class="role">Director</span></p>
  </div>

  <div class="contact-band">
    <p class="contact-line">
      <svg class="contact-icon" viewBox="0 0 16 16"><circle cx="8" cy="8" r="8" fill="#fff"/><path d="M5.2 4.3l1.3-.3.8 1.9-.9.7c.4 1 1.1 1.7 2 2l.7-.9 1.9.8-.3 1.3c-3 .3-5.8-2.5-5.5-5.5z" fill="#252525"/></svg>
      (555) 014-2280
    </p>
    <p class="contact-line">
      <svg class="contact-icon" viewBox="0 0 16 16"><circle cx="8" cy="8" r="8" fill="#fff"/><rect x="4" y="5" width="8" height="6" fill="#252525"/><path d="M4 5l4 3.2L12 5" stroke="#fff" stroke-width=".9" fill="none"/></svg>
      info@voltrisamail.com
    </p>
    <p class="contact-line">
      <svg class="contact-icon" viewBox="0 0 16 16"><circle cx="8" cy="8" r="8" fill="#fff"/><circle cx="8" cy="8" r="4.2" fill="none" stroke="#252525" stroke-width="1"/><path d="M3.8 8h8.4M8 3.8c-2 2.4-2 6 0 8.4M8 3.8c2 2.4 2 6 0 8.4" stroke="#252525" stroke-width=".9" fill="none"/></svg>
      www.voltrisaweb.com
    </p>
  </div>

  <div class="mark-notch"></div>
  <div class="mark-disc"></div>
</section>

<section class="card card-back">
  <div class="back-field" role="img" aria-label="Warm orange field where a faint repeating decorative pattern belongs"></div>
  <div class="back-brand">
    <span class="back-dot"></span>
    <span class="back-name">Voltrisa</span>
  </div>
</section>

</body>
</html>
```